Fun Billboard

I want a billboard with a fun picture of me (I'm attaching two options)

That will say:

#1 In Real Estate
#1 In Transparency

Marcus Thornby

Voted Corwin's Choice Realtor 2 years in a row!

Call/Text 410-555-0193

Then have my logo and the Corwin's Choice logo (attached)

and very small across the bottom:

The Lantern Group at Parkfield Real Estate, 2748 W Pellham Ave, Bel Air, MD 21014 833-555-0147

Billboard size is 14' tall by 48' wide

```html
<!DOCTYPE html>
<html lang="en">
<head>
<meta charset="utf-8">
<title>Marcus Thornby Billboard</title>
<link href="https://fonts.googleapis.com/css2?family=Montserrat:wght@300;400;600;700;800;900&display=swap" rel="stylesheet">
<style>
  :root {
    --navy: #1f2f5c;
    --navy-light: #34497d;
    --orange: #ee7a2f;
    --grey: #a9abae;
    --grey-light: #c3c5c8;
    --white: #ffffff;
    --panel: #eeeff1;
    --ink-dark: #1a1c22;
    --stage: #e4e6ea;
  }
  * { box-sizing: border-box; margin: 0; padding: 0; }
  html, body {
    width: 1200px; height: 970px; overflow: hidden;
    background: var(--stage);
    font-family: "Montserrat", sans-serif;
  }
  .billboard {
    position: absolute; left: 40px; top: 321px;
    width: 1120px; height: 327px;
    background: linear-gradient(100deg, var(--navy-light) 20%, var(--navy) 60%);
    overflow: hidden;
  }
  .info-band {
    position: absolute; left: 0; right: 0; bottom: 0; height: 72px;
    background: linear-gradient(180deg, var(--grey-light), var(--grey));
  }
  .brand-panel {
    position: absolute; left: 0; top: 0; width: 215px; height: 255px;
    background: linear-gradient(180deg, var(--white), var(--panel));
  }
  .brand-mark {
    position: absolute; left: 0; top: 40px; width: 215px;
    text-align: center; color: var(--navy);
  }
  .brand-mark .dot {
    display: block; width: 34px; height: 34px; margin: 0 auto 12px;
    border-radius: 50%; background: var(--navy);
  }
  .brand-name {
    font-weight: 600; font-size: 18px; letter-spacing: 0.5px;
    text-transform: uppercase; line-height: 1.1;
  }
  .brand-sub {
    font-weight: 600; font-size: 7px; letter-spacing: 1.2px;
    text-transform: uppercase; margin-top: 5px;
    border-top: 1px solid var(--navy); border-bottom: 1px solid var(--navy);
    display: inline-block; padding: 3px 4px;
  }
  .agent-shield {
    position: absolute; left: 28px; top: 170px; width: 158px; height: 120px;
  }
  .agent-name {
    position: absolute; left: 28px; top: 190px; width: 158px;
    text-align: center; color: var(--white);
    font-weight: 700; font-size: 19px; line-height: 1.15; text-transform: uppercase;
  }
  .agent-photo {
    position: absolute; left: 215px; top: 0; width: 225px; height: 327px;
    background: linear-gradient(180deg, #3a3f4a 0%, #2a2d35 55%, #e9a2b6 75%, #d9899f 100%);
  }
  .headline {
    position: absolute; left: 452px; top: 22px; height: 140px; color: var(--white);
    display: flex; align-items: center; white-space: nowrap;
  }
  .headline .rank {
    font-weight: 900; font-size: 140px; line-height: 1; letter-spacing: -6px;
    margin-right: 20px;
  }
  .headline .lines { display: block; line-height: 1; }
  .headline .line-bold {
    display: block; font-weight: 800; font-size: 45px;
    text-transform: uppercase; letter-spacing: -0.5px;
  }
  .headline .line-light {
    display: block; font-weight: 300; font-size: 41px;
    text-transform: uppercase; letter-spacing: 0.5px; margin-top: 6px;
  }
  .award-bar {
    position: absolute; left: 445px; right: 30px; top: 168px; height: 38px;
    background: var(--orange); color: var(--white);
    font-weight: 700; font-size: 18px; text-transform: uppercase; white-space: nowrap;
    display: flex; align-items: center; justify-content: center; letter-spacing: 0.3px;
  }
  .contact-line {
    position: absolute; right: 30px; top: 210px; color: var(--white);
    font-size: 36px; line-height: 44px; text-transform: uppercase; white-space: nowrap;
  }
  .contact-line .label { font-weight: 400; }
  .contact-line .phone { font-weight: 800; margin-left: 12px; }
  .award-badge {
    position: absolute; left: 458px; top: 214px; width: 98px; height: 98px;
  }
  .address {
    position: absolute; left: 580px; right: 30px; top: 268px;
    color: var(--white); font-size: 13px; font-weight: 400;
    text-align: center; line-height: 1.35; white-space: nowrap;
  }
</style>
</head>
<body>
  <main class="billboard">
    <div class="info-band"></div>

    <section class="brand-panel">
      <div class="brand-mark">
        <span class="dot"></span>
        <div class="brand-name">The Lantern Group</div>
        <div class="brand-sub">at Parkfield Real Estate</div>
      </div>
    </section>

    <svg class="agent-shield" viewBox="0 0 158 120" aria-hidden="true">
      <path d="M0 0 H158 V72 L79 120 L0 72 Z" fill="var(--navy)"/>
      <path d="M6 6 H152 V69 L79 113 L6 69 Z" fill="none" stroke="#3d5288" stroke-width="2"/>
    </svg>
    <div class="agent-name">Marcus<br>Thornby</div>

    <div class="agent-photo" role="img" aria-label="Photo of Marcus Thornby in a dark suit, holding a pink inflatable flamingo pool float"></div>

    <h1 class="headline">
      <span class="rank">#1</span>
      <span class="lines">
        <span class="line-bold">In Real Estate</span>
        <span class="line-light">In Transparency</span>
      </span>
    </h1>

    <div class="award-bar">Voted Corwin's Choice Realtor 2 years in a row!</div>

    <div class="contact-line"><span class="label">Call/Text</span><span class="phone">410-555-0193</span></div>

    <svg class="award-badge" viewBox="0 0 100 100" role="img" aria-label="Award badge">
      <circle cx="50" cy="50" r="48" fill="var(--ink-dark)"/>
      <circle cx="50" cy="50" r="41" fill="none" stroke="var(--white)" stroke-width="2"/>
    </svg>

    <p class="address">The Lantern Group at Parkfield Real Estate, 2748 W Pellham Ave,<br>Bel Air, MD 21014 833-555-0147</p>
  </main>
</body>
</html>
```